Mobile Repair Service on location needs a Web Design

We are starting a new mobile device repair service called Gadget Haven and our website needs a design!

Hello Designers!
First, we'd like to make clear this is more than a simple web design contest, we want the designers to create an idea. We want someone who can create the whole theme of the service's we provide. We want someone that can help design our visual branding, help us communicate a sentiment. And we are willing to pay for that.

Who are we?
Our company is based in Rotterdam, the Netherlands. We provide different services for all kinds of electronic devices. The kind of services we provide are, among other things, installations of hardware and software and the repair of broken or malfunctioning devices.
We are starting a new service that offers mobile device repairs on location, be it at the home of our customers, their office, or any other place. Just give us the address and we will come to you for the repair job. This is also our main USP. We have multiple skilled engineers who drive trough the country on a daily basis and can be on location within a working day. Repair is done immediately onsite while the customer waits. At this stage we will start with the smartphone product-group within the mobile devices. In a second phase we might also add tablets.
People don't want to be without their phone for weeks because of some parts that needed to be ordered by a repair center they had to sent their phone to. We offer a fully functional mobile repair center in the form of specially customized vans. These vans have all the tools and utilities needed by our engineers to safely repair your mobile device. Your phone is being repaired directly in front of you, the next business-day, on a location you desire.

For this new service we are creating a website called Gadget Haven. The website needs a story and matching design and this is where you come in. We are not looking for a simple template design we can get from any place. We need a story. We want you to create an idea, build a unique theme or vision that helps sell the product/service. This goes beyond the design of the website. We need the whole package, the design you are creating needs to have returning elements like icons, color use, images, maybe even characters etc. You name it! There needs to be a common thread in the design so we can reuse elements in, for example, the email templates, the work order or receipt we give to our customers (we may contact the winner of the contest to design these for us as well!).

The name 'Gadget Haven' is chosen. Haven (short for rehabilitate) has a bold and playful tone to it and the design needs to reflect the name. So we're looking for a somewhat playful and cheeky design. Definitely not too serious and definitely modern. We already got a logo that we love and that fit's this description (see attached design documents for the logo). It's bold, powerful and fun. Our web design needs to reflect this as well and has to fit in with our logo.
We would really like it if the design somehow incorporates elements that highlight our unique selling points (repairs on location, we come to you etc.). We would really like some form of story telling in the design. Think clumsy people breaking their phones. Teenagers in tears because they have no access to their friends. People nowadays have the need to always be 'connected'. What happens when your phone is broken or malfunctioning? We're handling tech, we are nerds and a little bit weird, but we're professionals and here to help you with your problem. The sentiment Wire Troop tries to communicate is something we really like. We're looking for fresh idea's, anything goes!

In an overview all Unique Selling Points of the Gadget haven service:
- Professional service on location. Don’t ship to us we will come to you!
- Clear pricing upfront. No hidden cost.
- Next business-day repair.
- Backed by a professional call center open 12 hours a day and open on a Saturday as well
- Backed by a professional repair center with more then 12 years of experience
- Repair is done by certified engineers
- 1 year warranty on the repair

The process:
The main function of our website will be for customers to make a repair request. A customer will visit our website and can make a repair request immediately by going through a 'request-order-flow'. In this flow he or she will need to fill in some forms and can select wich type/model/brand of mobile device he or she has and what parts need to be repaired. After a request is placed we will call the customer back (within an hour) for a short intake and to set a date/time and location. Our engineer will meet the customer at the specified location and will repair the device onsite in one of our mobile repair centers, which is a specialized van equipped with all the tools needed for device restorations.
So in short the steps are:
- Choose your device and repair job
- Place the order
- Get a callback within the hour
- Set date and location
- We will come to you.

Website functionality:
Our website is our main form of communication. So the sentiment we want to communicate needs be reflected in the design. We need a main/front page designed (preferably a long scrolling page design) containing:
1. Customers will be able to request a repair job directly on our website. So there will need to be a prominent button/link at the top of our main page that will bring the customer to this 'request-order-flow'. This is the main flow which needs to be full focus on the front page. All other items are secondary.
2. The general information of who we are and what we do, and why the customer should choose us. Preferably in short bullet-point type keywords/sentences with icons or other visual cues. See our unique selling points to get an idea of the information that will be displayed here.
3. There needs to be a section that will explain the process (see above) of a repair request step-by- step, again in brief short key sentences and with (custom) icons.
4. There needs to be a section that explains to the customer he/she can always contact us if they are not sure what the problem is with their device, and for this reason are not sure what repair request they should order.
5. We want to implement some functionality that display customer ratings or customer reviews. So there needs to be room for some kind of widget of plugin we're going to implement which shows these reviews.
6. A 'For business section' where we will explain all the options we provide for corporate clients.
7. Social media links.
8. There needs to be a menu with buttons that leads to the all sections described in the previous points.

For now, we need a design for our front page. In the second phase, when we have picked our winner, we may ask the winner to design the page(s) for our request workflow as well.

EDIT:
Finally, we have a very specific order in mind for the different segments of our website. We would like you to add some more segments that were not in our original brief as well:

1. Top header with order/request button. (should instantly make clear our main USP, we do repairs on location)
2. Our process
3. Our unique selling points / why choose us
4. The kind of repairs we do (broken screens, broken batteries, water damage, broken camera's, no sound etc.)
5. A 'meet our team' section, where we introduce some of our engineers
6. A 'contact us for any questions' section/
7. Testimonials/user reviews
8. A section where we show key performance indicators
9. 'For businesses' sections
10.'Subscribe for newsletter' field
11. Social media buttons

Industry/Entity Type

It Service

Number of Pages Required

1 page

Font styles to use
Sans Serif

Requirements
Must have
• a main/front page, design only
• custom icons/images for banners, adverts online and in print (high res)
Nice to have
• Storytelling in our design.
• Design that fits with our brand new logo.
• Elements like icons to have a flat design.
• Keep in mind that the website will need to be responsive when designing! (Ideally provide an example of the mobile design as well)
• Create a fun and trustworthy feeling.

```html
<!DOCTYPE html>
<html lang="en">
<head>
<meta charset="utf-8">
<title>Gadget Haven – Mobile repairs on location</title>
<link href="https://fonts.googleapis.com/css2?family=Roboto:wght@300;400;500;700&display=swap" rel="stylesheet">
<style>
:root{
  --orange:#ef6a3c;
  --orange-soft:#f7a584;
  --teal:#147e92;
  --teal-light:#3a97a8;
  --navy:#1d2030;
  --ink:#2f3033;
  --muted:#77797e;
  --line:#e3e4e6;
  --grey-bg:#f2f2f3;
  --white:#ffffff;
  --green:#41b36a;
}
*{box-sizing:border-box;margin:0;padding:0}
html,body{width:1200px;height:3814px;overflow:hidden}
body{font-family:'Roboto',Arial,sans-serif;color:var(--ink);background:var(--white);position:relative}
.section{position:absolute;left:0;width:1200px}
.abs{position:absolute}
.accent{position:absolute;width:36px;height:2px;background:var(--orange)}
.title{font-weight:300;font-size:26px;color:var(--ink)}
.center{text-align:center;left:0;width:1200px}
.small{font-size:12px;line-height:19px;color:#55575c}

/* header */
.site-header{top:0;height:76px;background:var(--white);border-bottom:1px solid #eee}
.brand{left:89px;top:18px;display:flex;align-items:center;gap:9px}
.brand-dot{width:34px;height:34px;border-radius:50%;background:var(--orange)}
.brand-name{font-weight:700;font-size:15px;line-height:16px;color:var(--navy);width:70px}
.nav{left:313px;top:29px;display:flex;gap:0;font-size:13px;color:#55575c}
.nav span{margin-right:28px}
.order-btn{left:810px;top:20px;width:128px;height:36px;border-radius:18px;background:var(--orange);color:#fff;font-size:13px;font-weight:500;text-align:center;line-height:36px}
.location-note{left:958px;top:29px;font-size:12px;color:var(--muted);display:flex;align-items:center;gap:6px}

/* hero */
.hero{top:76px;height:404px;background:linear-gradient(#fbfbfb,#f1f1f2)}
.hero h1{left:89px;top:150px;font-weight:300;font-size:31px;color:var(--ink)}
.hero .sub{left:89px;top:190px;font-size:15px;color:var(--muted)}
.outline-btn{border:1px solid var(--orange);color:var(--orange);border-radius:20px;font-size:12px;text-align:center}
.hero .outline-btn{left:89px;top:236px;width:142px;height:38px;line-height:36px}
.art-buildings{left:780px;top:60px;width:420px;height:344px;background:linear-gradient(#f1f1f2,#e6e6e8);opacity:.8}
.art-van{left:390px;top:262px;width:305px;height:128px;border-radius:14px;background:linear-gradient(#ffffff,#dfe0e3)}
.art-house{left:740px;top:48px;width:300px;height:356px;background:linear-gradient(#f07a4e,#e25a2c);border-radius:6px 6px 0 0}

/* process */
.process-band{top:480px;height:262px;background:var(--orange)}
.process-band .accent{left:582px;top:52px;background:#fff}
.process-band .title{top:64px;color:#fff}
.grey-block{top:742px;height:568px;background:var(--grey-bg)}
.process-card{left:89px;top:605px;width:1022px;height:257px;background:#fff;box-shadow:0 6px 24px rgba(0,0,0,.08)}
.process-line{position:absolute;left:100px;top:96px;width:820px;height:1px;background:var(--line)}
.step{position:absolute;top:56px;width:160px;text-align:center}
.step .icon{width:80px;height:80px;margin:0 auto;border-radius:50%;background:#fff;border:1px solid var(--line);display:flex;align-items:center;justify-content:center}
.step p{margin-top:22px;font-size:13px;line-height:21px;color:#55575c}

/* about */
.phone{left:150px;top:912px;width:235px;height:398px;background:#fff;border-radius:26px 26px 0 0;box-shadow:0 8px 30px rgba(0,0,0,.1)}
.phone-screen{position:absolute;left:14px;top:48px;width:207px;height:350px;background:#fafafa;border:1px solid #eee}
.app{position:absolute;width:38px;height:38px;border-radius:8px}
.about .accent{left:505px;top:932px}
.about .title{left:505px;top:943px}
.usp-list{left:505px;top:994px;list-style:none}
.usp-list li{display:flex;align-items:center;gap:12px;height:35.5px;font-size:12px;color:#55575c}
.tick{width:14px;height:14px;border-radius:3px;background:#dbe8e0;display:flex;align-items:center;justify-content:center}

/* repairs */
.repairs{top:1310px;height:363px;background:#fff}
.repairs .accent{left:582px;top:80px}
.repairs .title{top:92px}
.repairs .sub{top:134px;font-size:12px;color:var(--muted)}
.repair{position:absolute;top:180px;width:160px;text-align:center}
.repair .icon{width:90px;height:90px;margin:0 auto;border-radius:50%;background:#fff;border:1px solid var(--line);display:flex;align-items:center;justify-content:center}
.repair .icon.active{border:none;box-shadow:0 6px 20px rgba(0,0,0,.14)}
.repair p{margin-top:18px;font-size:13px;color:#55575c}

/* team */
.team{top:1673px;height:455px;background:var(--grey-bg)}
.team .accent{left:89px;top:80px}
.team .title{left:89px;top:90px}
.member-name{left:89px;top:150px;font-weight:700;font-size:14px}
.team .bio{left:89px;top:180px;width:420px}
.team .divider{left:89px;top:335px;width:420px;height:1px;background:#d9dadc}
.team .qual{left:89px;top:352px;font-size:12px;color:#55575c}
.profile{position:absolute;overflow:hidden;box-shadow:0 10px 28px rgba(0,0,0,.18)}
.profile .photo{position:absolute;inset:0}
.profile h3{position:absolute;left:0;width:100%;text-align:center;color:#fff;font-weight:700;font-size:19px}
.profile-btn{position:absolute;left:60px;top:260px;width:148px;height:36px;border-radius:18px;background:#fff;font-size:12px;line-height:36px;text-align:center;color:var(--ink)}
.next-arrow{left:1165px;top:195px}

/* contact */
.contact{top:2128px;height:218px;background:var(--teal)}
.contact .accent{left:89px;top:66px}
.contact .title{left:89px;top:76px;color:#fff;font-size:28px}
.contact .small{left:89px;top:120px;width:560px;color:#d9eef2}
.contact-btn{left:985px;top:88px;width:126px;height:44px;border-radius:22px;background:var(--teal-light);color:#fff;font-size:13px;text-align:center;line-height:44px}

/* reviews */
.reviews{top:2346px;height:476px;background:linear-gradient(#ffffff,#f1f1f2)}
.reviews .accent{left:582px;top:68px}
.reviews .title{top:80px}
.review{position:absolute;top:150px;width:324px;height:234px;background:#fff;box-shadow:0 3px 14px rgba(0,0,0,.06);padding:32px 30px}
.review.raised{top:142px;box-shadow:0 10px 30px rgba(0,0,0,.14)}
.review .who{position:absolute;left:30px;top:150px;display:flex;align-items:center;gap:14px}
.avatar{width:46px;height:46px;border-radius:50%;background:linear-gradient(#6a6d75,#2e3038)}
.who b{display:block;font-size:12px;font-weight:500}
.who i{font-style:normal;font-size:10px;color:var(--muted)}
.quote{position:absolute;right:30px;top:150px;font-size:60px;font-weight:700;color:#e3e4e6;line-height:60px}
.dots{left:0;width:1200px;top:424px;display:flex;justify-content:center;gap:6px}
.dots span{width:6px;height:6px;border-radius:50%;background:#cfd0d3}
.dots span:first-child{background:var(--teal)}

/* kpi */
.kpi{top:2822px;height:465px;background:#fff}
.kpi .accent{left:582px;top:66px}
.kpi .title{top:78px}
.chart-card{position:absolute;top:128px;height:266px;background:#fff;box-shadow:0 3px 16px rgba(0,0,0,.08)}

/* business */
.business{top:3287px;height:399px;background:var(--grey-bg)}
.business .accent{left:89px;top:68px}
.business .title{left:89px;top:78px}
.business .p1{left:89px;top:124px;width:470px}
.business .p2{left:89px;top:200px;width:470px}
.business .outline-btn{left:89px;top:300px;width:124px;height:38px;line-height:36px}
.art-desk{left:720px;top:86px;width:390px;height:250px;background:linear-gradient(#f2f2f3,#e2e3e6);border-radius:8px}

/* footer */
.site-footer{top:3686px;height:128px;background:var(--navy)}
.site-footer .lead{left:89px;top:34px;color:#fff;font-size:14px}
.email-field{left:425px;top:26px;width:275px;height:32px;border-bottom:1px solid #5a5e70;font-size:11px;color:#8f93a3;line-height:30px}
.follow{left:920px;top:34px;color:#fff;font-size:13px;display:flex;align-items:center;gap:14px}
.social{width:10px;height:10px;border-radius:50%;background:#fff}
.to-top{left:1140px;top:38px;width:40px;height:40px;border-radius:50%;background:var(--orange);display:flex;align-items:center;justify-content:center}
.footer-rule{left:0;top:76px;width:1200px;height:1px;background:#2d3142}
.copyright{left:89px;top:94px;font-size:11px;color:#8f93a3}
</style>
</head>
<body>

<header class="section site-header">
  <div class="abs brand"><span class="brand-dot"></span><span class="brand-name">GADGET HAVEN</span></div>
  <nav class="abs nav"><span>About</span><span>Process</span><span>Contact</span><span>Customer Reviews</span><span>For Business</span></nav>
  <div class="abs order-btn">Order/Request</div>
  <div class="abs location-note"><svg width="9" height="12" viewBox="0 0 9 12"><path d="M4.5 0A4.5 4.5 0 0 0 0 4.5C0 8 4.5 12 4.5 12S9 8 9 4.5A4.5 4.5 0 0 0 4.5 0z" fill="#41b36a"/><circle cx="4.5" cy="4.5" r="1.6" fill="#fff"/></svg>We do repairs on location</div>
</header>

<section class="section hero">
  <div class="abs art-buildings" role="img" aria-label="Faint city buildings in the background"></div>
  <h1 class="abs">We provide different services</h1>
  <p class="abs sub">for all kinds of electronic devices</p>
  <div class="abs outline-btn">Contact us now</div>
  <div class="abs art-van" role="img" aria-label="White repair van parked in the street"></div>
  <div class="abs art-house" role="img" aria-label="Orange house with a customer waiting at the door"></div>
</section>

<section class="section process-band">
  <div class="accent"></div>
  <h2 class="abs title center">The Process</h2>
</section>
<div class="section grey-block"></div>

<div class="abs process-card">
  <div class="process-line"></div>
  <div class="step" style="left:21px"><div class="icon"><svg width="30" height="34" viewBox="0 0 30 34"><rect x="5" y="2" width="16" height="30" rx="3" fill="#3c3f48"/><rect x="7" y="6" width="12" height="20" fill="#fff"/><rect x="15" y="8" width="13" height="9" rx="2" fill="#ef6a3c"/></svg></div><p>Choose your device<br>and repair job</p></div>
  <div class="step" style="left:222px"><div class="icon"><svg width="30" height="34" viewBox="0 0 30 34"><rect x="4" y="2" width="22" height="30" rx="2" fill="#dfeee6"/><path d="M8 11l3 3 5-6" stroke="#41b36a" stroke-width="2" fill="none"/><rect x="8" y="20" width="14" height="2" fill="#41b36a"/><circle cx="23" cy="27" r="6" fill="#ef6a3c"/></svg></div><p>Place the<br>Order</p></div>
  <div class="step" style="left:431px"><div class="icon"><svg width="30" height="34" viewBox="0 0 30 34"><rect x="7" y="2" width="16" height="30" rx="3" fill="#3c3f48"/><rect x="9" y="6" width="12" height="20" fill="#f7a584"/><circle cx="15" cy="16" r="4" fill="#ef6a3c"/></svg></div><p>Get a callback<br>within an hour</p></div>
  <div class="step" style="left:640px"><div class="icon"><svg width="32" height="32" viewBox="0 0 32 32"><rect x="3" y="5" width="24" height="22" rx="2" fill="#fff" stroke="#3c3f48" stroke-width="2"/><rect x="3" y="5" width="24" height="6" fill="#ef6a3c"/><circle cx="24" cy="24" r="6" fill="#ef6a3c"/></svg></div><p>Set date &amp;<br>location</p></div>
  <div class="step" style="left:841px"><div class="icon"><svg width="32" height="30" viewBox="0 0 32 30"><path d="M16 3L3 14h4v13h18V14h4z" fill="#ef6a3c"/><rect x="13" y="18" width="6" height="9" fill="#147e92"/></svg></div><p>We will come<br>to you</p></div>
</div>

<section class="about">
  <div class="abs phone">
    <div class="phone-screen">
      <div class="app" style="left:12px;top:14px;background:#f5a623"></div>
      <div class="app" style="left:60px;top:14px;background:#6d6f75"></div>
      <div class="app" style="left:108px;top:14px;background:#e03c3c"></div>
      <div class="app" style="left:12px;top:64px;background:#e94b8a"></div>
      <div class="app" style="left:60px;top:64px;background:#f5a623"></div>
      <div class="app" style="left:108px;top:64px;background:#41b36a"></div>
      <div class="app" style="left:12px;top:114px;background:#2f9e62"></div>
      <div class="app" style="left:60px;top:114px;background:#f5a623"></div>
      <div class="app" style="left:12px;top:300px;background:#4aa3df"></div>
      <div class="app" style="left:60px;top:300px;background:#41b36a"></div>
      <div class="app" style="left:108px;top:300px;background:#e03c3c"></div>
    </div>
  </div>
  <div class="accent"></div>
  <h2 class="abs title">About the company</h2>
  <ul class="abs usp-list">
    <li><span class="tick"><svg width="8" height="7"><path d="M1 3.5l2 2 4-4" stroke="#41b36a" stroke-width="1.5" fill="none"/></svg></span>Professional service on location. Don't ship to us we will come to you!</li>
    <li><span class="tick"><svg width="8" height="7"><path d="M1 3.5l2 2 4-4" stroke="#41b36a" stroke-width="1.5" fill="none"/></svg></span>Clear pricing upfront. No hidden cost.</li>
    <li><span class="tick"><svg width="8" height="7"><path d="M1 3.5l2 2 4-4" stroke="#41b36a" stroke-width="1.5" fill="none"/></svg></span>Next business-day repair.</li>
    <li><span class="tick"><svg width="8" height="7"><path d="M1 3.5l2 2 4-4" stroke="#41b36a" stroke-width="1.5" fill="none"/></svg></span>Backed by a professional call center open 12 hours a day and open on a Saturday as well</li>
    <li><span class="tick"><svg width="8" height="7"><path d="M1 3.5l2 2 4-4" stroke="#41b36a" stroke-width="1.5" fill="none"/></svg></span>Backed by a professional repair center with more then 12 years of experience</li>
    <li><span class="tick"><svg width="8" height="7"><path d="M1 3.5l2 2 4-4" stroke="#41b36a" stroke-width="1.5" fill="none"/></svg></span>Repair is done by certified engineers</li>
    <li><span class="tick"><svg width="8" height="7"><path d="M1 3.5l2 2 4-4" stroke="#41b36a" stroke-width="1.5" fill="none"/></svg></span>1 year warranty on the repair</li>
  </ul>
</section>

<section class="section repairs">
  <div class="accent"></div>
  <h2 class="abs title center">Kind of Repairs we do</h2>
  <p class="abs sub center" style="text-align:center">We do almost every type of repairs on your location</p>
  <div class="repair" style="left:111px"><div class="icon"><svg width="22" height="36"><rect x="1" y="1" width="20" height="34" rx="3" fill="#3c3f48"/><rect x="3" y="5" width="16" height="24" fill="#9fb6c9"/></svg></div><p>Broken Screens</p></div>
  <div class="repair" style="left:313px"><div class="icon"><svg width="22" height="36"><rect x="1" y="1" width="20" height="34" rx="3" fill="#3c3f48"/><rect x="3" y="5" width="16" height="24" fill="#41b36a"/></svg></div><p>Broken Batteries</p></div>
  <div class="repair" style="left:520px"><div class="icon active"><svg width="22" height="36"><rect x="1" y="1" width="20" height="34" rx="3" fill="#3c3f48"/><rect x="3" y="5" width="16" height="24" fill="#ef6a3c"/></svg></div><p>Water Damage</p></div>
  <div class="repair" style="left:727px"><div class="icon"><svg width="22" height="36"><rect x="1" y="1" width="20" height="34" rx="3" fill="#3c3f48"/><circle cx="7" cy="8" r="3" fill="#9aa0ad"/></svg></div><p>Broken Cameras</p></div>
  <div class="repair" style="left:930px"><div class="icon"><svg width="22" height="36"><rect x="1" y="1" width="20" height="34" rx="3" fill="#3c3f48"/><rect x="3" y="5" width="16" height="24" fill="#e9e3cf"/></svg></div><p>No Sound</p></div>
</section>

<section class="section team">
  <div class="accent"></div>
  <h2 class="abs title">Meet The Team</h2>
  <p class="abs member-name">Daniel Verhoef</p>
  <div class="abs bio small">
    <p>Aenean vulputate eleifend tellus aenean leo ligula porttitor eu consequat vitae eleifend ac enim aliquam lorem ante dapibus in viverra quis feugiat a tellus phasellus viverra nulla ut metus varius laoreet.</p>
    <p style="margin-top:12px">Leo ligula porttitor eu consequat vitae eleifend ac enim aliquam lorem ante dapibus in viverra quis feugiat a tellus phasellus.</p>
  </div>
  <div class="abs divider"></div>
  <p class="abs qual">Qualification goes here with some other info...</p>

  <div class="profile" style="left:593px;top:72px;width:268px;height:318px">
    <div class="photo" role="img" aria-label="Portrait photo of engineer Daniel Verhoef" style="background:linear-gradient(#c9cfd4,#4d5966)"></div>
    <h3 style="top:60px">Daniel Verhoef</h3>
    <div class="profile-btn">View full Profile &nbsp;→</div>
  </div>
  <div class="profile" style="left:885px;top:72px;width:226px;height:270px">
    <div class="photo" role="img" aria-label="Photo of engineer Ruben Maas standing by the sea" style="background:linear-gradient(#d8dee2,#5c7f94)"></div>
    <h3 style="top:38px">Ruben Maas</h3>
  </div>
  <div class="profile" style="left:1135px;top:72px;width:65px;height:240px;opacity:.45">
    <div class="photo" role="img" aria-label="Photo of the next team member" style="background:linear-gradient(#e6eaed,#9aacb8)"></div>
  </div>
  <svg class="abs next-arrow" width="20" height="16" viewBox="0 0 20 16"><path d="M2 8h15M11 2l6 6-6 6" stroke="#2f3033" stroke-width="1.6" fill="none"/></svg>
</section>

<section class="section contact">
  <div class="accent"></div>
  <h2 class="abs title">Contact us for any questions</h2>
  <p class="abs small">You can always contact us if you are not sure what the problem is with your device, and you are not sure what repair request you should order.</p>
  <div class="abs contact-btn">Contact us</div>
</section>

<section class="section reviews">
  <div class="accent"></div>
  <h2 class="abs title center">Customer Reviews</h2>
  <article class="review" style="left:89px">
    <p class="small">Aenean vulputate eleifend tellus aenean leo ligula porttitor eu, consequat vitae eleifend ac enim aliquam lorem ante dapibus in viverra quis feugiat a tellus.</p>
    <div class="who"><span class="avatar" role="img" aria-label="Customer avatar"></span><span><b>Lena Starke</b><i>@lena</i></span></div>
    <span class="quote">“</span>
  </article>
  <article class="review raised" style="left:440px">
    <p class="small">Aenean vulputate eleifend tellus aenean leo ligula porttitor eu, consequat vitae eleifend ac enim aliquam lorem ante dapibus in viverra quis feugiat a tellus.</p>
    <div class="who"><span class="avatar" role="img" aria-label="Customer avatar"></span><span><b>Tom Dekker</b><i>@tom</i></span></div>
    <span class="quote">“</span>
  </article>
  <article class="review" style="left:787px">
    <p class="small">Aenean vulputate eleifend tellus aenean leo ligula porttitor eu, consequat vitae eleifend ac enim aliquam lorem ante dapibus in viverra quis feugiat a tellus.</p>
    <div class="who"><span class="avatar" role="img" aria-label="Customer avatar"></span><span><b>Sam Jansen</b><i>@sam</i></span></div>
    <span class="quote">“</span>
  </article>
  <div class="abs dots"><span></span><span></span><span></span></div>
</section>

<section class="section kpi">
  <div class="accent"></div>
  <h2 class="abs title center">Key Performance Indicators</h2>
  <div class="chart-card" style="left:89px;width:500px">
    <svg width="500" height="266" viewBox="0 0 500 266" font-family="Roboto, sans-serif" font-size="9" fill="#9a9ca1">
      <line x1="268" y1="22" x2="300" y2="22" stroke="#b9b4e0" stroke-width="2"/><text x="306" y="25">Indicator 1</text>
      <line x1="360" y1="22" x2="392" y2="22" stroke="#ef6a3c" stroke-width="2"/><text x="398" y="25">Indicator 2</text>
      <g stroke="#eceded">
        <line x1="50" y1="60" x2="460" y2="60"/><line x1="50" y1="90" x2="460" y2="90"/><line x1="50" y1="120" x2="460" y2="120"/><line x1="50" y1="150" x2="460" y2="150"/><line x1="50" y1="180" x2="460" y2="180"/><line x1="50" y1="210" x2="460" y2="210"/><line x1="50" y1="240" x2="460" y2="240"/>
        <line x1="50" y1="60" x2="50" y2="240"/><line x1="101" y1="60" x2="101" y2="240"/><line x1="152" y1="60" x2="152" y2="240"/><line x1="203" y1="60" x2="203" y2="240"/><line x1="254" y1="60" x2="254" y2="240"/><line x1="305" y1="60" x2="305" y2="240"/><line x1="356" y1="60" x2="356" y2="240"/><line x1="407" y1="60" x2="407" y2="240"/><line x1="460" y1="60" x2="460" y2="240"/>
      </g>
      <text x="28" y="63">0.7</text><text x="28" y="93">0.6</text><text x="28" y="123">0.5</text><text x="28" y="153">0.4</text><text x="28" y="183">0.3</text><text x="28" y="213">0.2</text><text x="28" y="243">0.1</text>
      <polyline points="50,225 101,178 152,196 203,164 254,170 305,138 356,160 407,150 460,70" fill="none" stroke="#b9b4e0" stroke-width="2"/>
      <polyline points="50,232 101,210 152,130 203,185 254,115 305,155 356,100 407,150 460,128" fill="none" stroke="#ef6a3c" stroke-width="2"/>
    </svg>
  </div>
  <div class="chart-card" style="left:613px;width:498px">
    <svg width="498" height="266" viewBox="0 0 498 266" font-family="Roboto, sans-serif" font-size="9" fill="#9a9ca1">
      <line x1="150" y1="22" x2="182" y2="22" stroke="#b9b4e0" stroke-width="2"/><text x="188" y="25">Indicator 1</text>
      <line x1="244" y1="22" x2="276" y2="22" stroke="#147e92" stroke-width="2"/><text x="282" y="25">Indicator 2</text>
      <line x1="338" y1="22" x2="370" y2="22" stroke="#ef6a3c" stroke-width="2"/><text x="376" y="25">Indicator 3</text>
      <g stroke="#eceded">
        <line x1="30" y1="60" x2="470" y2="60"/><line x1="30" y1="240" x2="470" y2="240"/>
        <line x1="30" y1="60" x2="30" y2="240"/><line x1="85" y1="60" x2="85" y2="240"/><line x1="140" y1="60" x2="140" y2="240"/><line x1="195" y1="60" x2="195" y2="240"/><line x1="250" y1="60" x2="250" y2="240"/><line x1="305" y1="60" x2="305" y2="240"/><line x1="360" y1="60" x2="360" y2="240"/><line x1="415" y1="60" x2="415" y2="240"/><line x1="470" y1="60" x2="470" y2="240"/>
      </g>
      <rect x="30" y="100" width="62" height="30" fill="#b9b4e0"/>
      <rect x="30" y="152" width="158" height="30" fill="#147e92"/>
      <rect x="30" y="204" width="305" height="30" fill="#ef6a3c"/>
    </svg>
  </div>
</section>

<section class="section business">
  <div class="accent"></div>
  <h2 class="abs title">For Business</h2>
  <p class="abs small p1">In enim justo rhoncus ut imperdiet a venenatis vitae, justo nullam dictum felis eu pede mollis pretium integer tincidunt cras dapibus. Vivamus elementum semper nisi aenean vulputate.</p>
  <p class="abs small p2">Maecenas nec odio et ante tincidunt tempus donec vitae sapien ut libero venenatis faucibus nullam quis ante etiam sit amet orci eget eros faucibus tincidunt duis leo sed fringilla mauris sit.</p>
  <div class="abs outline-btn">Learn More</div>
  <div class="abs art-desk" role="img" aria-label="Office worker at a desk with a laptop in front of a shelf of equipment"></div>
</section>

<footer class="section site-footer">
  <p class="abs lead">Subscribe to our email newsletter</p>
  <div class="abs email-field">Enter email address...
    <svg style="position:absolute;right:0;top:10px" width="12" height="12" viewBox="0 0 12 12"><path d="M0 5L12 0 7 12 5.5 6.5z" fill="#ef6a3c"/></svg>
  </div>
  <div class="abs follow">Follow us:
    <span class="social" role="img" aria-label="Social network link"></span>
    <span class="social" role="img" aria-label="Social network link"></span>
    <span class="social" role="img" aria-label="Social network link"></span>
    <span class="social" role="img" aria-label="Social network link"></span>
  </div>
  <div class="abs to-top"><svg width="12" height="14" viewBox="0 0 12 14"><path d="M6 13V2M1 6l5-5 5 5" stroke="#fff" stroke-width="1.8" fill="none"/></svg></div>
  <div class="abs footer-rule"></div>
  <p class="abs copyright">© 2017, All Rights Reserved.</p>
</footer>

</body>
</html>
```